Harbinger Cargo needs a business card design.

Design a double-sided business card for new freight business. On the front, would like to see our logo along with the following info:

Malcolm Strathby
CEO/FOUNDER
555-207-4163
malcolmstrathby@harbinger-cargo.example

On the reverse side, we would like to use the graphic image of our logo only without the Harbinger Cargo name.

```html
<!DOCTYPE html>
<html lang="en">
<head>
<meta charset="utf-8">
<title>Harbinger Cargo — Business Card</title>
<link rel="stylesheet" href="https://fonts.googleapis.com/css2?family=Archivo+Black&family=Roboto:wght@300;400&display=swap">
<style>
  :root {
    --navy: #020564;
    --red: #b00808;
    --white: #ffffff;
    --ink: #2a2a2a;
    --backdrop: #e6e6e9;
  }
  * { margin: 0; padding: 0; box-sizing: border-box; }
  html, body { width: 1200px; height: 900px; overflow: hidden; }
  body {
    background: var(--backdrop);
    position: relative;
    font-family: "Roboto", Arial, sans-serif;
  }
  .card {
    position: absolute;
    left: 250px;
    width: 700px;
    height: 400px;
    overflow: hidden;
    box-shadow: 0 6px 18px rgba(0,0,0,0.18);
  }
  .card--back { top: 35px; background: var(--navy); display: flex; align-items: center; justify-content: center; }
  .card--front { top: 465px; background: var(--white); }

  .brand-mark {
    width: 150px; height: 150px;
    border-radius: 50%;
    background: var(--red);
    margin-left: 30px;
  }

  .brand {
    font-family: "Archivo Black", "Arial Black", sans-serif;
    letter-spacing: 0.08em;
    text-transform: uppercase;
    line-height: 1.05;
  }
  .brand--front {
    position: absolute; top: 48px; right: 40px;
    color: var(--navy); font-size: 30px;
    display: flex; align-items: center; gap: 14px;
  }
  .brand-dot { width: 18px; height: 18px; border-radius: 50%; background: var(--red); flex: none; }

  .person { position: absolute; top: 70px; left: 55px; }
  .person-name { font-family: "Archivo Black", "Arial Black", sans-serif; font-size: 25px; letter-spacing: 0.04em; text-transform: uppercase; color: var(--navy); }
  .person-name .surname { color: var(--red); }
  .person-role { font-weight: 300; font-size: 20px; color: var(--ink); letter-spacing: 0.03em; margin-top: 2px; }

  .wave { position: absolute; inset: 0; width: 700px; height: 400px; }

  .contacts { position: absolute; left: 60px; top: 198px; list-style: none; }
  .contacts li { display: flex; align-items: center; gap: 10px; font-size: 17px; color: var(--ink); margin-bottom: 6px; }
  .contacts svg { width: 20px; height: 20px; fill: var(--red); flex: none; }

  .website { position: absolute; right: 40px; bottom: 50px; color: var(--white); font-size: 17px; letter-spacing: 0.01em; }
</style>
</head>
<body>
  <section class="card card--back" aria-label="Card reverse">
    <div class="brand-mark" role="img" aria-label="Harbinger Cargo brand mark"></div>
  </section>

  <section class="card card--front" aria-label="Card front">
    <svg class="wave" viewBox="0 0 700 400" aria-hidden="true">
      <path d="M0 318 C250 322 430 285 580 200 C400 310 220 345 0 348 Z" fill="var(--red)"/>
      <path d="M0 356 C240 352 430 305 560 232 C610 205 660 182 700 176 L700 400 L0 400 Z" fill="var(--navy)"/>
    </svg>

    <div class="person">
      <h1 class="person-name">Malcolm <span class="surname">Strathby</span></h1>
      <p class="person-role">CEO/FOUNDER</p>
    </div>

    <div class="brand brand--front">
      <span class="brand-dot"></span>
      <span>Harbinger<br>Cargo</span>
    </div>

    <ul class="contacts">
      <li>
        <svg viewBox="0 0 24 24" aria-hidden="true"><path d="M6.6 10.8a15.1 15.1 0 0 0 6.6 6.6l2.2-2.2a1 1 0 0 1 1-.25 11.4 11.4 0 0 0 3.6.57 1 1 0 0 1 1 1V20a1 1 0 0 1-1 1A17 17 0 0 1 3 4a1 1 0 0 1 1-1h3.5a1 1 0 0 1 1 1c0 1.250.2 2.45.57 3.57a1 1 0 0 1-.25 1z"/></svg>
        555-207-4163
      </li>
      <li>
        <svg viewBox="0 0 24 24" aria-hidden="true"><path d="M2 5h20v14H2z M3 6.5v.4l9 6 9-6v-.4z" fill-rule="evenodd"/></svg>
        malcolmstrathby@harbinger-cargo.example
      </li>
    </ul>

    <p class="website">www.harbinger-cargo.example</p>
  </section>
</body>
</html>
```